Seeking a new website design for electrical contracting company

Pelham & Tracy electrical contracting needs a new website for pelham-tracy.com

We are looking for modern and something real cool with motion for a landing page. we have some cool images from our photo shoot. maybe even 3d motion our existing logo. we would like something we can edit with news and events and update a past project page. Also allow to take payment
stock images at
https://mirabelwhitfordphotography.pixfolio-example.com/Pelham-and-Tracy

Target Market(s)

construction , home owners , business owners,

Industry/Entity Type

construction , electrical

Coding

Coded - Design and coding required

Number of Pages Required

5+ page

Font styles to use
Serif
Sans Serif

Colors
0054AA
0677BA
7BADD7
CADEEF
E8F1F8
0094D4
00A9DD
6FCCEA
C7EBF8
E9F6FB
FFF300
FFF600
FEFA6F
FFFEC7
FFFEE8

Requirements
Must have
• excitement, motion, selling professionalism,

```html
<!DOCTYPE html>
<html lang="en">
<head>
<meta charset="utf-8">
<title>Pelham &amp; Tracy — Electrical Contracting</title>
<link rel="stylesheet" href="https://fonts.googleapis.com/css2?family=Josefin+Sans:wght@600;700&family=Poppins:wght@400;500;600;700&display=swap">
<style>
:root{
  --navy:#1b2a5e;
  --navy-deep:#111c45;
  --orange:#f7931e;
  --orange-dark:#e07c0c;
  --white:#ffffff;
  --ink:#2d3450;
  --muted:#6b7088;
  --pale:#eef0f8;
  --line:#d7dbe8;
}
*{box-sizing:border-box;margin:0;padding:0}
html,body{width:1200px;height:4980px;overflow:hidden}
body{font-family:"Poppins",sans-serif;color:var(--ink);background:var(--white);position:relative}
.abs{position:absolute}
h1,h2,h3{font-family:"Josefin Sans",sans-serif;font-weight:700}
.btn{display:inline-block;font-family:"Poppins",sans-serif;font-weight:600;font-size:13px;letter-spacing:.5px;color:var(--white);padding:12px 26px;text-transform:uppercase}
.btn-orange{background:var(--orange)}
.btn-navy{background:var(--navy)}
.section-title{position:absolute;left:0;width:1200px;text-align:center;font-size:40px;color:var(--navy);letter-spacing:1px}

/* header */
.site-header{left:0;top:0;width:1200px;height:92px;background:var(--white);z-index:5}
.brand{left:40px;top:14px;display:flex;align-items:center;gap:12px;background:var(--white);padding:10px 18px 14px;z-index:6}
.brand-mark{width:26px;height:26px;background:var(--orange)}
.brand-name{font-family:"Josefin Sans",sans-serif;font-weight:700;font-size:26px;color:var(--navy);letter-spacing:.5px}
.topbar{left:560px;top:0;width:640px;height:40px;background:var(--navy);display:flex;align-items:center;gap:40px;padding-left:130px;color:var(--white);font-size:13px}
.topbar span{display:flex;align-items:center;gap:8px}
.topbar svg{width:16px;height:16px}
.main-nav{left:500px;top:52px;display:flex;gap:34px;font-size:13px;font-weight:600;color:var(--navy);text-transform:uppercase}
.main-nav .active{color:var(--orange);border-bottom:2px solid var(--orange);padding-bottom:4px}

/* hero */
.hero{left:0;top:0;width:1200px;height:640px;background:radial-gradient(ellipse at 78% 45%,#f0a24a 0%,#8a5a3a 14%,#2b3f6e 38%,#121c3c 70%,#0a1028 100%)}
.hero-title{left:140px;top:280px;font-size:44px;line-height:1.2;color:var(--white);letter-spacing:1.5px;text-transform:uppercase}
.hero-title em{font-style:normal;color:var(--orange)}
.hero-cta{left:140px;top:460px;display:flex;gap:14px}
.hero-edge{left:0;top:540px;width:1200px;height:140px}

/* about */
.about{left:0;top:640px;width:1200px;height:560px;background:linear-gradient(180deg,#ffffff 0%,#f4f5fa 100%)}
.about-brand{left:140px;top:120px;width:360px;height:300px;display:flex;align-items:center;justify-content:center;gap:14px}
.about-brand .brand-mark{width:40px;height:40px}
.about-brand .brand-name{font-size:36px}
.about-title{left:590px;top:60px;font-size:38px;color:var(--navy);letter-spacing:1px}
.about-text{left:590px;top:120px;width:520px;font-size:12.5px;line-height:1.85;color:var(--muted)}
.about-cta{left:590px;top:370px;display:flex;gap:14px}

/* services */
.services{left:0;top:1200px;width:1200px;height:780px;background:var(--pale)}
.services-bands{left:0;top:0;width:1200px;height:780px}
.hex{position:absolute;width:290px;height:370px;clip-path:polygon(50% 0,100% 25%,100% 75%,50% 100%,0 75%,0 25%)}
.hex-label{position:absolute;top:215px;left:45px;width:200px;padding:8px 0;text-align:center;font-size:14px;font-weight:600;letter-spacing:1px;color:var(--navy);background:rgba(255,255,255,.85);text-transform:uppercase}
.hex-label.on{background:var(--orange);color:var(--white)}
.arrow-btn{width:44px;height:44px;border-radius:50%;background:var(--white);border:1px solid var(--line);display:flex;align-items:center;justify-content:center}

/* news */
.news{left:0;top:1980px;width:1200px;height:680px;background:var(--white)}
.news-feature{left:150px;top:150px;width:440px;height:370px;background:linear-gradient(135deg,#6d7d96 0%,#3a4a6a 50%,#a64a2c 100%)}
.news-feature-card{width:250px;height:200px;background:var(--white);padding:18px;box-shadow:0 6px 18px rgba(0,0,0,.15)}
.news-item{left:620px;width:440px;height:170px;background:var(--white);border-left:4px solid var(--orange);box-shadow:0 4px 16px rgba(20,30,70,.12);padding:20px 24px}
.news-head{font-size:12px;font-weight:700;color:var(--navy);line-height:1.5;text-transform:uppercase}
.news-meta{font-size:11px;font-weight:600;color:var(--navy);margin:10px 0 8px}
.news-body{font-size:11px;color:var(--muted);line-height:1.6}
.read-more{display:inline-block;margin-top:8px;font-size:11px;font-weight:700;color:var(--navy);border-bottom:2px solid var(--orange);text-transform:uppercase}
.news-cta{left:500px;top:560px}

/* projects */
.projects{left:0;top:2660px;width:1200px;height:1100px;background:var(--white)}
.tile{position:absolute}
.plus{position:absolute;left:250px;top:200px;width:40px;height:40px;border-radius:50%;background:var(--orange);color:var(--white);font-size:26px;line-height:40px;text-align:center;font-weight:600}
.projects-cta{left:480px;top:1030px}

/* contact */
.contact{left:0;top:3760px;width:1200px;height:800px;background:var(--navy)}
.contact-title{left:630px;top:220px;font-size:38px;color:var(--white);letter-spacing:1px}
.contact-form{left:630px;top:290px;width:430px;display:grid;grid-template-columns:1fr 1fr;gap:16px}
.field{background:var(--white);height:46px;padding:14px 16px;font-size:12px;color:var(--muted)}
.field.wide{grid-column:1 / 3;height:110px}
.submit{grid-column:1 / 2;justify-self:start}

/* footer */
.site-footer{left:0;top:4560px;width:1200px;height:420px;background:var(--white)}
.foot-brand{left:0;top:40px;width:1200px;display:flex;justify-content:center;align-items:center;gap:12px}
.foot-contact{left:200px;top:150px;width:800px;display:flex;justify-content:space-between;font-size:14px;font-weight:500;color:var(--navy)}
.foot-contact span{display:flex;align-items:center;gap:12px}
.foot-icon{width:34px;height:34px;border-radius:50%;background:var(--orange);display:flex;align-items:center;justify-content:center}
.foot-nav{left:0;top:220px;width:1200px;display:flex;justify-content:center;gap:34px;font-size:12px;font-weight:600;color:var(--navy);text-transform:uppercase}
.copyright{left:0;top:265px;width:1200px;text-align:center;font-size:11px;color:var(--muted)}
.social{left:0;top:320px;width:1200px;display:flex;justify-content:center;gap:12px}
.social i{display:block;width:30px;height:30px;border-radius:50%;background:var(--navy)}
</style>
</head>
<body>

<!-- HERO -->
<section class="hero abs" role="img" aria-label="Electrician welding with bright sparks against a dark blue industrial backdrop"></section>
<h1 class="hero-title abs">Powering the<br><em>Southeast with</em><br>Precision &amp; Pride</h1>
<div class="hero-cta abs"><a class="btn btn-orange">Our Work</a><a class="btn btn-navy">Get a Quote</a></div>

<!-- HEADER -->
<header class="site-header abs">
  <div class="topbar abs">
    <span><svg viewBox="0 0 24 24" fill="#f7931e"><path d="M6.6 10.8a15.1 15.1 0 0 0 6.6 6.6l2.2-2.2a1 1 0 0 1 1-.25 11.4 11.4 0 0 0 3.6.57 1 1 0 0 1 1 1V20a1 1 0 0 1-1 1A17 17 0 0 1 3 4a1 1 0 0 1 1-1h3.5a1 1 0 0 1 1 1c0 1.25.2 2.45.57 3.57a1 1 0 0 1-.25 1z"/></svg>1-555-017-4420</span>
    <span><svg viewBox="0 0 24 24"><path d="M3 5h18v14H3z" fill="none" stroke="#f7931e" stroke-width="2"/><path d="M3 6l9 7 9-7" fill="none" stroke="#f7931e" stroke-width="2"/></svg>info@pelham-tracy.com</span>
  </div>
  <nav class="main-nav abs">
    <span class="active">Home</span><span>About Us</span><span>Services</span><span>Projects</span><span>News and Events</span><span>Contact Us</span>
  </nav>
</header>
<div class="brand abs"><i class="brand-mark"></i><span class="brand-name">Pelham &amp; Tracy</span></div>

<!-- ABOUT -->
<section class="about abs">
  <div class="about-brand abs"><i class="brand-mark"></i><span class="brand-name">Pelham &amp; Tracy</span></div>
  <h2 class="about-title abs">ABOUT US</h2>
  <p class="about-text abs">Pelham &amp; Tracy delivers dependable electrical contracting for homes, businesses and industrial sites across the region. Our licensed crews plan, install and maintain power systems with careful attention to safety, code and schedule. From new construction wiring to service upgrades, lighting design and emergency repairs, we bring the same precision to every job. We keep clients informed from the first walkthrough to the final inspection, and we stand behind our work long after the lights come on.</p>
  <div class="about-cta abs"><a class="btn btn-orange">More</a><a class="btn btn-navy">Get a Quote</a></div>
</section>

<svg class="hero-edge abs" viewBox="0 0 1200 140" preserveAspectRatio="none">
  <polygon points="0,60 600,100 1200,60 1200,140 0,140" fill="#ffffff"/>
  <polyline points="0,58 600,98 1200,58" fill="none" stroke="#1b2a5e" stroke-width="10"/>
  <polyline points="0,66 600,106 1200,66" fill="none" stroke="#f7931e" stroke-width="4"/>
  <rect x="585" y="70" width="30" height="30" fill="#f7931e" transform="rotate(45 600 85)"/>
</svg>

<!-- SERVICES -->
<section class="services abs">
  <svg class="services-bands abs" viewBox="0 0 1200 780" preserveAspectRatio="none">
    <polygon points="0,0 1200,0 1200,40 600,110 0,40" fill="#ffffff"/>
    <polygon points="0,700 600,640 1200,700 1200,780 0,780" fill="#ffffff"/>
    <polyline points="0,640 300,600 600,630" fill="none" stroke="#d7dbe8" stroke-width="2"/>
    <polyline points="600,630 900,600 1200,640" fill="none" stroke="#d7dbe8" stroke-width="2"/>
  </svg>
  <h2 class="section-title" style="top:125px">OUR SERVICES</h2>
  <div class="hex" style="left:140px;top:205px;background:linear-gradient(180deg,#9bb4d4 0%,#7a7266 60%,#3f4a5e 100%)" role="img" aria-label="Modern residential home at dusk"><span class="hex-label">Residential</span></div>
  <div class="hex" style="left:455px;top:205px;background:linear-gradient(180deg,#2f6fb3 0%,#6fa9dd 45%,#1b3f7a 100%)" role="img" aria-label="Glass commercial towers seen from below"><span class="hex-label on">Commercial</span></div>
  <div class="hex" style="left:770px;top:205px;background:linear-gradient(180deg,#566274 0%,#8a8f9c 50%,#2f3646 100%)" role="img" aria-label="Industrial plant with steel piping"><span class="hex-label">Industrial</span></div>
  <div class="arrow-btn abs" style="left:62px;top:368px"><svg width="14" height="14" viewBox="0 0 14 14"><path d="M9 2 4 7l5 5" fill="none" stroke="#1b2a5e" stroke-width="2"/></svg></div>
  <div class="arrow-btn abs" style="left:1094px;top:368px"><svg width="14" height="14" viewBox="0 0 14 14"><path d="M5 2l5 5-5 5" fill="none" stroke="#1b2a5e" stroke-width="2"/></svg></div>
</section>

<!-- NEWS -->
<section class="news abs">
  <h2 class="section-title" style="top:60px">NEWS AND EVENTS</h2>
  <div class="news-feature abs" role="img" aria-label="Electricians at work on switchgear with stacked equipment"></div>
  <article class="news-feature-card abs" style="left:200px;top:320px">
    <h3 class="news-head">Nemo enim ipsam voluptatem quia ute irure dolo</h3>
    <p class="news-meta">April 18,2023 &nbsp;|&nbsp; Comments</p>
    <p class="news-body">Crews finished a full panel upgrade and new lighting for a local school.</p>
    <a class="read-more">Read More</a>
  </article>
  <article class="news-item abs" style="top:150px">
    <h3 class="news-head">Nemo enim ipsam voluptatem quia ute irure</h3>
    <p class="news-meta">April 18,2023 &nbsp;|&nbsp; Comments</p>
    <p class="news-body">Join our team at the regional builders expo for live safety demos.</p>
    <a class="read-more">Read More</a>
  </article>
  <article class="news-item abs" style="top:350px">
    <h3 class="news-head">Nemo enim ipsam voluptatem quia ute irure</h3>
    <p class="news-meta">April 18,2023 &nbsp;|&nbsp; Comments</p>
    <p class="news-body">We welcome three new licensed electricians to our growing service team.</p>
    <a class="read-more">Read More</a>
  </article>
  <a class="btn btn-orange news-cta abs">View More News</a>
</section>

<!-- PROJECTS -->
<section class="projects abs">
  <h2 class="section-title" style="top:30px">FEATURED PROJECTS</h2>
  <div class="tile" style="left:0;top:100px;width:352px;height:456px;background:linear-gradient(180deg,#9fb6d2 0%,#dfe3ea 55%,#8d939c 100%)" role="img" aria-label="White industrial enclosure under blue sky"></div>
  <div class="tile" style="left:370px;top:100px;width:540px;height:456px;background:linear-gradient(135deg,#3b5590 0%,#6a7fb0 40%,#c08a52 100%)" role="img" aria-label="Worker in hard hat installing wiring, blue tinted">
    <span class="plus">+</span>
  </div>
  <div class="tile" style="left:928px;top:100px;width:272px;height:456px;background:linear-gradient(180deg,#2f3b56 0%,#c66a2c 55%,#1c2438 100%)" role="img" aria-label="Industrial plant lit in warm light"></div>
  <div class="tile" style="left:0;top:572px;width:288px;height:416px;background:linear-gradient(180deg,#1c2a52 0%,#d86a2c 70%,#2a1e1e 100%)" role="img" aria-label="Refinery towers at sunset"></div>
  <div class="tile" style="left:304px;top:572px;width:416px;height:416px;background:linear-gradient(180deg,#2a3a66 0%,#7a4a3a 50%,#f0a050 80%,#3a2a22 100%)" role="img" aria-label="Family home with warm lights at dusk"></div>
  <div class="tile" style="left:736px;top:572px;width:464px;height:416px;background:linear-gradient(180deg,#d9c8a8 0%,#a48b6a 55%,#5e4c3a 100%)" role="img" aria-label="Bright modern living room with recessed lighting"></div>
  <a class="btn btn-orange projects-cta abs">View More Projects</a>
</section>

<!-- CONTACT -->
<section class="contact abs">
  <svg class="abs" style="left:0;top:0" width="1200" height="800" viewBox="0 0 1200 800">
    <defs>
      <linearGradient id="sparks" x1="0" y1="0" x2="1" y2="1">
        <stop offset="0" stop-color="#5a5f6e"/><stop offset=".55" stop-color="#f2a040"/><stop offset="1" stop-color="#3a2a1e"/>
      </linearGradient>
    </defs>
    <polygon points="0,0 1200,0 1200,30 420,160 0,70" fill="#ffffff"/>
    <polyline points="0,70 420,160 1200,30" fill="none" stroke="#f7931e" stroke-width="6"/>
    <polygon points="0,90 420,180 260,800 0,800" fill="url(#sparks)" role="img" aria-label="Grinder throwing orange sparks"/>
    <polygon points="420,180 460,188 310,800 260,800" fill="#f7931e"/>
    <polygon points="0,780 1200,700 1200,800 0,800" fill="#ffffff"/>
    <polyline points="0,780 1200,700" fill="none" stroke="#f7931e" stroke-width="6"/>
  </svg>
  <h2 class="contact-title abs">CONTACT US</h2>
  <form class="contact-form abs">
    <div class="field">First Name</div>
    <div class="field">Last Name</div>
    <div class="field">Email address</div>
    <div class="field">Phone Number</div>
    <div class="field wide">Message</div>
    <a class="btn btn-orange submit">Submit Message</a>
  </form>
</section>

<!-- FOOTER -->
<footer class="site-footer abs">
  <div class="foot-brand abs"><i class="brand-mark"></i><span class="brand-name">Pelham &amp; Tracy</span></div>
  <div class="foot-contact abs">
    <span><i class="foot-icon"><svg width="16" height="16" viewBox="0 0 24 24" fill="#fff"><path d="M6.6 10.8a15.1 15.1 0 0 0 6.6 6.6l2.2-2.2a1 1 0 0 1 1-.25 11.4 11.4 0 0 0 3.6.57 1 1 0 0 1 1 1V20a1 1 0 0 1-1 1A17 17 0 0 1 3 4a1 1 0 0 1 1-1h3.5a1 1 0 0 1 1 1c0 1.25.2 2.45.57 3.57a1 1 0 0 1-.25 1z"/></svg></i>1-555-017-4420</span>
    <span><i class="foot-icon"><svg width="16" height="16" viewBox="0 0 24 24"><rect x="3" y="5" width="18" height="14" fill="none" stroke="#fff" stroke-width="2"/><path d="M3 6l9 7 9-7" fill="none" stroke="#fff" stroke-width="2"/></svg></i>info@pelham-tracy.com</span>
    <span><i class="foot-icon"><svg width="16" height="16" viewBox="0 0 24 24" fill="#fff"><path d="M12 2a7 7 0 0 0-7 7c0 5 7 13 7 13s7-8 7-13a7 7 0 0 0-7-7zm0 9.5A2.5 2.5 0 1 1 12 6.5a2.5 2.5 0 0 1 0 5z"/></svg></i>48 Alder Lane, Brookhaven NH 03000</span>
  </div>
  <nav class="foot-nav abs"><span>Home</span><span>About Us</span><span>Services</span><span>Projects</span><span>News and Events</span><span>Contact Us</span></nav>
  <p class="copyright abs">© 2023 Pelham &amp; Tracy All Rights Reserved &nbsp;|&nbsp; Privacy Policy &nbsp;|&nbsp; Terms of Use</p>
  <div class="social abs"><i></i><i></i><i></i><i></i><i></i></div>
</footer>

</body>
</html>
```